Financial industry/Advisor business card

I'm a Financial Advisor starting my own investment company, Brantley Wealth Management. I currently use the 'Light Blue' color that's provided on the Cardwise web page, but I want something unique. I'd like to keep the color, but the design is up for grabs.

Industry/Entity Type

Business

Contact Information for Business Card

Brantley Wealth Management
Dean R. Brantley
President
5129 Willowgate Ln
Ste 240
Hollis Bend NC 28406
555-372-6140-Office
555-372-6187-Fax
DBRANTLEY@BRANTWM.example

```html
<!DOCTYPE html>
<html lang="en">
<head>
<meta charset="utf-8">
<title>Brantley Wealth Management — Business Card</title>
<link rel="stylesheet" href="https://fonts.googleapis.com/css2?family=Oswald:wght@400;500;700&display=swap">
<style>
  :root {
    --backdrop: #e9ecef;
    --card-white: #ffffff;
    --ink: #2b2b2b;
    --brand-blue: #1f9ad6;
    --light-blue: #6cc0e8;
    --steel-blue: #4a8db8;
    --deep-blue: #0f5e92;
    --mid-blue: #2a7fb8;
    --back-blue-top: #3aa6d8;
    --back-blue-bottom: #1a7fb6;
    --back-text: #d9dde0;
  }
  * { box-sizing: border-box; margin: 0; padding: 0; }
  html, body { width: 1200px; height: 871px; overflow: hidden; }
  body {
    background: var(--backdrop);
    font-family: "Oswald", "Arial Narrow", sans-serif;
    display: flex;
    align-items: center;
    justify-content: center;
    gap: 40px;
  }
  .card {
    width: 560px;
    height: 320px;
    position: relative;
    overflow: hidden;
    box-shadow: 0 6px 20px rgba(0,0,0,0.18);
  }
  .card--back {
    background: linear-gradient(160deg, var(--back-blue-top), var(--back-blue-bottom));
    display: flex;
    align-items: center;
    justify-content: center;
  }
  .card--back .brand-name {
    color: var(--back-text);
    font-weight: 500;
    font-size: 34px;
    letter-spacing: 4px;
    text-transform: uppercase;
    text-align: center;
    line-height: 1.25;
  }
  .card--front { background: var(--card-white); }
  .front-brand {
    position: absolute;
    left: 30px;
    top: 80px;
    width: 240px;
    display: flex;
    align-items: center;
    gap: 12px;
  }
  .front-brand .brand-mark {
    width: 22px; height: 22px;
    background: var(--brand-blue);
    flex: none;
  }
  .front-brand .brand-name {
    color: var(--brand-blue);
    font-weight: 500;
    font-size: 24px;
    letter-spacing: 2px;
    text-transform: uppercase;
    line-height: 1.15;
  }
  .divider {
    position: absolute;
    left: 285px;
    top: 30px;
    width: 2px;
    height: 200px;
    background: var(--brand-blue);
  }
  .contact {
    position: absolute;
    left: 305px;
    top: 36px;
    right: 12px;
    color: var(--ink);
  }
  .contact .person {
    font-weight: 700;
    font-size: 27px;
    letter-spacing: 1.5px;
    line-height: 1.1;
  }
  .contact .title {
    color: var(--brand-blue);
    font-weight: 500;
    font-size: 13px;
    letter-spacing: 2px;
    line-height: 1.3;
    margin-bottom: 8px;
  }
  .contact-row {
    display: flex;
    align-items: flex-start;
    gap: 8px;
    font-size: 14px;
    font-weight: 500;
    letter-spacing: 1px;
    line-height: 1.35;
    margin-bottom: 3px;
    white-space: nowrap;
  }
  .contact-row svg { width: 14px; height: 14px; flex: none; margin-top: 3px; fill: var(--brand-blue); }
  .bands {
    position: absolute;
    left: 0; right: 0; bottom: 0;
    height: 44px;
    display: flex;
    gap: 4px;
  }
  .band--light { background: var(--light-blue); flex: 0.9; }
  .band--steel { background: var(--steel-blue); flex: 1.1; }
  .band--deep { background: var(--deep-blue); flex: 1.4; }
  .band--mid { background: var(--mid-blue); flex: 1.1; }
</style>
</head>
<body>
  <section class="card card--back" aria-label="Card back">
    <p class="brand-name">Brantley<br>Wealth Management</p>
  </section>

  <section class="card card--front" aria-label="Card front">
    <div class="front-brand">
      <span class="brand-mark"></span>
      <p class="brand-name">Brantley<br>Wealth Management</p>
    </div>
    <div class="divider"></div>
    <div class="contact">
      <h1 class="person">Dean R. Brantley</h1>
      <p class="title">PRESIDENT</p>
      <div class="contact-row">
        <svg viewBox="0 0 24 24" aria-hidden="true"><path d="M12 2a7 7 0 0 0-7 7c0 5 7 13 7 13s7-8 7-13a7 7 0 0 0-7-7zm0 9.5A2.5 2.5 0 1 1 12 6.5a2.5 2.5 0 0 1 0 5z"/></svg>
        <span>5129 Willowgate Ln Ste 240<br>Hollis Bend NC 28406</span>
      </div>
      <div class="contact-row">
        <svg viewBox="0 0 24 24" aria-hidden="true"><path d="M3 8c0-2 4-4 9-4s9 2 9 4v2h-5V8.5c-2-.7-6-.7-8 0V10H3zm2 4h14l1 8H4z"/></svg>
        <span>555-372-6140</span>
      </div>
      <div class="contact-row">
        <svg viewBox="0 0 24 24" aria-hidden="true"><path d="M6 2h9l3 3v5h2a2 2 0 0 1 2 2v8a2 2 0 0 1-2 2H4a2 2 0 0 1-2-2v-8a2 2 0 0 1 2-2h2zm2 2v6h8V6h-3V4zm-2 11v2h4v-2z"/></svg>
        <span>555-372-6187</span>
      </div>
      <div class="contact-row">
        <svg viewBox="0 0 24 24" aria-hidden="true"><path d="M2 5h20v14H2zm2 2v.5l8 5.5 8-5.5V7zm0 3v7h16v-7l-8 5.5z"/></svg>
        <span>DBRANTLEY@BRANTWM.example</span>
      </div>
    </div>
    <div class="bands">
      <div class="band band--light"></div>
      <div class="band band--steel"></div>
      <div class="band band--deep"></div>
      <div class="band band--mid"></div>
    </div>
  </section>
</body>
</html>
```